Printing Business Card

I would like the colorful accents of my business to match with an artistic design. The idea is that I would like to have a creative mix so that I am making a embossed, suede card to show off with marketing events.

```html
<!DOCTYPE html>
<html lang="en">
<head>
<meta charset="utf-8">
<title>Keystone Print Co. — Business Card</title>
<link rel="stylesheet" href="https://fonts.googleapis.com/css2?family=Montserrat:wght@400;600;700&family=Yellowtail&family=Libre+Baskerville:ital,wght@0,400;1,700&display=swap">
<style>
  :root {
    --stage: #2b2b2b;
    --card-black: #050505;
    --card-white: #ffffff;
    --ink: #111111;
    --cyan: #1e96e3;
    --magenta: #df1a7e;
    --text-light: #ffffff;
    --rule: #8a8a8a;
  }
  * { margin: 0; padding: 0; box-sizing: border-box; }
  html, body { width: 1200px; height: 880px; overflow: hidden; }
  body {
    background: var(--stage);
    position: relative;
    font-family: "Montserrat", sans-serif;
  }
  .card {
    position: absolute;
    border-radius: 18px;
    overflow: hidden;
  }
  .card-back {
    left: 70px; top: 280px;
    width: 560px; height: 320px;
    background: var(--card-black);
    display: flex; align-items: center; justify-content: center;
  }
  .brand {
    display: flex; align-items: center; gap: 12px;
    font-family: "Montserrat", sans-serif;
    font-weight: 700;
    font-size: 30px;
    letter-spacing: 0.5px;
  }
  .brand-dot {
    width: 22px; height: 22px; border-radius: 50%;
    flex: none;
  }
  .card-back .brand { color: var(--text-light); }
  .card-back .brand-dot { background: var(--text-light); }

  .card-front {
    left: 770px; top: 160px;
    width: 320px; height: 560px;
    background: var(--card-white);
  }
  .card-front .shapes { position: absolute; inset: 0; }
  .card-front .brand {
    position: absolute; left: 0; right: 0; top: 110px;
    justify-content: center;
    color: var(--ink);
    font-size: 24px;
  }
  .card-front .brand-dot { background: var(--ink); width: 18px; height: 18px; }

  .contact {
    position: absolute; left: 24px; top: 326px; width: 180px;
    color: var(--text-light);
  }
  .person-name {
    font-family: "Yellowtail", cursive;
    font-size: 27px; line-height: 1;
    white-space: nowrap;
  }
  .person-role {
    font-family: "Libre Baskerville", serif;
    font-size: 11px; margin: 4px 0 0 62px;
  }
  .contact-rule {
    border: 0; border-top: 1px solid var(--rule);
    margin: 10px 0 10px;
  }
  .contact-label {
    font-family: "Libre Baskerville", serif;
    font-style: italic; font-weight: 700;
    font-size: 11px;
  }
  .contact-value {
    font-size: 13px; margin: 2px 0 8px;
    white-space: nowrap;
  }
  .web {
    position: absolute; left: 0; right: 0; bottom: 14px;
    text-align: center; color: var(--text-light);
    font-size: 17px; letter-spacing: 0.5px;
  }
</style>
</head>
<body>
  <section class="card card-back" aria-label="Card back">
    <div class="brand"><span class="brand-dot"></span>Keystone Print Co.</div>
  </section>

  <section class="card card-front" aria-label="Card front">
    <svg class="shapes" width="320" height="560" viewBox="0 0 320 560" aria-hidden="true">
      <path d="M0,212 C140,222 270,300 320,410 L320,440 C262,320 140,250 0,236 Z" fill="var(--cyan)"/>
      <path d="M0,238 C150,250 272,330 320,440 L320,504 L0,504 Z" fill="var(--card-black)"/>
      <path d="M70,262 C180,280 270,350 310,440" fill="none" stroke="var(--card-white)" stroke-width="2"/>
      <rect x="0" y="504" width="320" height="6" fill="var(--card-white)"/>
      <rect x="0" y="510" width="320" height="50" fill="var(--magenta)"/>
    </svg>

    <div class="brand"><span class="brand-dot"></span>Keystone Print Co.</div>

    <div class="contact">
      <p class="person-name">Nora L. Bennett</p>
      <p class="person-role">Manager</p>
      <hr class="contact-rule">
      <p class="contact-label">Phone:</p>
      <p class="contact-value">+1 555 210 4837</p>
      <p class="contact-label">Email:</p>
      <p class="contact-value">hello@keystoneprint.com</p>
    </div>

    <p class="web">www.keystoneprint.com</p>
  </section>
</body>
</html>
```